Bramble Artisan Wood Fired Pizza business card design

I have a logo and need an eye catching design that will get me noticed.
My business is wood fired pizza. I want a bold design that will make our customers remember us and the food that we serve. Work with the colors of our logo and texts. Maybe add designs that lend to what or how pizza is made using our wood fired oven?

Target Market(s)

Foodies!

Contact Information for Business Card

Bramble Artisan Wood Fired Pizza
Our slogan is Fast. Fresh. Handcrafted
Catering for all events

Requirements
Must have
• Noel Pruett
Telephone 570 555 0187
website www.trybramble.com
Facebook @trybramblepizza maybe use the facebook logo next to it
Instagram trybramblepizza maybe use the instagram logo next to it
Catering for all events
Nice to have
• Maybe pizza peels, pizza cutters? Wood? Fired wood? Using our flame in the background?
Please work with different colored text so each sentence stands out? A themed color for facebook?
Maybe work with the colors within our logo?
Please try to use the our bramble font, but not a must have.

```html
<!DOCTYPE html>
<html lang="en">
<head>
<meta charset="utf-8">
<title>Bramble Artisan Wood Fired Pizza — Business Card</title>
<link href="https://fonts.googleapis.com/css2?family=Staatliches&family=Oswald:wght@400;500&display=swap" rel="stylesheet">
<style>
  :root {
    --page: #262626;
    --card: #1d1d1d;
    --gold: #f0ae2a;
    --gold-deep: #c27e16;
    --gold-dark: #8a5a12;
    --red: #e2313b;
    --white: #ededed;
    --yellow: #f4c21c;
    --muted: #cfcfcf;
  }
  * { box-sizing: border-box; margin: 0; padding: 0; }
  html, body { width: 1200px; height: 900px; overflow: hidden; background: var(--page); }
  .canvas { position: relative; width: 1200px; height: 900px; }

  .card {
    position: absolute; left: 250px; width: 700px; height: 400px;
    background: var(--card); overflow: hidden;
    box-shadow: 0 14px 32px rgba(0,0,0,.5);
    font-family: "Staatliches", "Oswald", sans-serif; color: var(--white);
  }
  .card--front { top: 30px; }
  .card--back { top: 470px; }

  /* illustration areas: crisp-edged regions with a warm gold gradient */
  .art { position: absolute; inset: 0; }
  .art--slices {
    background: linear-gradient(135deg, var(--gold) 0%, var(--gold-deep) 55%, var(--gold-dark) 100%);
  }
  .art--toppings {
    background: linear-gradient(315deg, var(--gold) 0%, var(--gold-deep) 60%, var(--gold-dark) 100%);
  }
  .art--scatter {
    background: linear-gradient(90deg, var(--gold-deep), var(--gold));
    opacity: .75;
  }

  .card--front .art--slices { clip-path: polygon(0 20%, 33% 12%, 35% 30%, 24% 75%, 0 82%); }
  .card--front .art--toppings { clip-path: polygon(100% 28%, 92% 42%, 88% 66%, 80% 88%, 66% 100%, 100% 100%); }
  .card--front .art--scatter { clip-path: polygon(36% 0, 50% 0, 47% 10%, 38% 14%); }

  .card--back .art--slices { clip-path: polygon(100% 8%, 68% 16%, 66% 40%, 76% 88%, 100% 94%); }
  .card--back .art--toppings { clip-path: polygon(0 86%, 22% 92%, 46% 90%, 60% 100%, 0 100%); }
  .card--back .art--scatter { clip-path: polygon(0 0, 16% 0, 12% 10%, 0 14%); }

  .brand { position: absolute; display: flex; flex-direction: column; align-items: center; }
  .brand__mark { border-radius: 50%; background: var(--red); }
  .brand__tag { font-family: "Oswald", sans-serif; font-weight: 500; letter-spacing: 2px; color: var(--white); }
  .brand__name { letter-spacing: 6px; line-height: 1; color: var(--white); }
  .brand__rule { height: 2px; background: var(--gold); }
  .brand__est { font-family: "Oswald", sans-serif; font-size: 8px; letter-spacing: 2px; color: var(--muted); margin-top: 3px; }

  .card--front .brand { left: 300px; top: 26px; width: 260px; }
  .card--front .brand__mark { width: 34px; height: 34px; margin-bottom: 6px; }
  .card--front .brand__tag { font-size: 10px; }
  .card--front .brand__name { font-size: 44px; }
  .card--front .brand__rule { width: 210px; margin-top: 4px; }

  .person { position: absolute; left: 250px; top: 160px; font-size: 46px; font-weight: 400; letter-spacing: 5px; color: var(--white); line-height: 1; }

  .contacts {
    position: absolute; left: 250px; top: 226px; display: grid;
    grid-template-columns: auto auto; column-gap: 28px; row-gap: 8px;
    font-family: "Oswald", sans-serif; font-size: 12.5px; letter-spacing: 1.5px; color: var(--white);
  }
  .contact { display: flex; align-items: center; gap: 8px; }
  .contact__icon { width: 16px; height: 16px; flex: none; }

  .slogan { position: absolute; font-size: 24px; letter-spacing: 2px; line-height: 1.1; }
  .slogan__main { color: var(--white); }
  .slogan__sub { color: var(--yellow); font-size: 21px; }
  .card--front .slogan { left: 250px; top: 290px; }

  .card--back .brand { left: 70px; top: 56px; width: 340px; }
  .card--back .brand__mark { width: 48px; height: 48px; margin-bottom: 8px; }
  .card--back .brand__tag { font-size: 13px; }
  .card--back .brand__name { font-size: 70px; }
  .card--back .brand__rule { width: 300px; margin-top: 4px; }
  .card--back .slogan { left: 70px; top: 262px; }
</style>
</head>
<body>
<main class="canvas">
  <section class="card card--front">
    <div class="art art--slices" role="img" aria-label="Gold line sketch of pizza slices with toppings"></div>
    <div class="art art--scatter" role="img" aria-label="Scattered sketched olives and garlic"></div>
    <div class="art art--toppings" role="img" aria-label="Gold line sketch of mushrooms, olives, garlic and basil leaves"></div>

    <div class="brand">
      <span class="brand__mark"></span>
      <span class="brand__tag">ARTISAN WOOD FIRED PIZZA</span>
      <span class="brand__name">BRAMBLE</span>
      <span class="brand__rule"></span>
      <span class="brand__est">EST. 2020</span>
    </div>

    <h1 class="person">NOEL PRUETT</h1>

    <div class="contacts">
      <span class="contact">
        <svg class="contact__icon" viewBox="0 0 16 16"><circle cx="8" cy="8" r="7.5" fill="none" stroke="var(--gold)"/><path d="M5 4.5c.5-.4 1-.3 1.3.2l.7 1.2c.2.4 0 .8-.3 1 .4.9 1.1 1.6 2 2 .2-.3.6-.5 1-.3l1.2.7c.5.3.6.8.2 1.3-1.2 1.2-3.4.3-5-1.3S3.8 5.7 5 4.5z" fill="var(--gold)"/></svg>
        570 555 0187
      </span>
      <span class="contact">
        <svg class="contact__icon" viewBox="0 0 16 16"><circle cx="8" cy="8" r="7" fill="var(--gold)"/></svg>
        WWW.TRYBRAMBLE.COM
      </span>
      <span class="contact">
        <svg class="contact__icon" viewBox="0 0 16 16"><circle cx="8" cy="8" r="7" fill="var(--gold)"/></svg>
        TRYBRAMBLEPIZZA
      </span>
      <span class="contact">
        <svg class="contact__icon" viewBox="0 0 16 16"><circle cx="8" cy="8" r="7" fill="var(--gold)"/></svg>
        @TRYBRAMBLEPIZZA
      </span>
    </div>

    <p class="slogan">
      <span class="slogan__main">FAST. FRESH. HANDCRAFTED</span><br>
      <span class="slogan__sub">CATERING FOR ALL EVENTS</span>
    </p>
  </section>

  <section class="card card--back">
    <div class="art art--slices" role="img" aria-label="Gold line sketch of pizza slices"></div>
    <div class="art art--scatter" role="img" aria-label="Scattered sketched olives and garlic"></div>
    <div class="art art--toppings" role="img" aria-label="Gold line sketch of mushrooms, olives and garlic"></div>

    <div class="brand">
      <span class="brand__mark"></span>
      <span class="brand__tag">ARTISAN WOOD FIRED PIZZA</span>
      <span class="brand__name">BRAMBLE</span>
      <span class="brand__rule"></span>
      <span class="brand__est">EST. 2020</span>
    </div>

    <p class="slogan">
      <span class="slogan__main">FAST. FRESH. HANDCRAFTED</span><br>
      <span class="slogan__sub">CATERING FOR ALL EVENTS</span>
    </p>
  </section>
</main>
</body>
</html>
```